PREVENTING FALLS IN YOUR HOME / MAKING YOUR HOME SAFER

We sell, and install grab bars for only $99 each in the home. Statistics to present: 2.8 million people are treated in emergency rooms annually for falls. 800,000 are hospitalized because of fall injury. 95% of hip fractures are caused by falling. I would like a 1 page marketing piece containing a cartoon like male slipping backwards holding on to shower curtain which is bending curtain rod that cannot support him. Then as a don't and do,same man wisely entering tub using grab bar. Slipping on stairs, trying to grab onto whatever won't hold him would be another scenario.
Included in piece would be above fall statistics separated into bursts, reminder that grab bars can be installed in any room including the garage and a star burst of Only $99, includes bar and installation and

Target Market(s)

over 50 year old market butpredominantly elderly population

Industry/Entity Type

Home Health Care

Font styles to use
Sans Serif

Colors
ec1f27

Requirements
Must have
• instant recognition that a grab bar can prevent serious falls and hip fracture. The cartoon characterization must make instant understanding without reading text
Nice to have
• large print
• concise message
• not a lot of reading to understand
• cartoons in circle with line through don' t circle Ie. no swimming
Should not have
• small print
• congested page

```html
<!DOCTYPE html>
<html lang="en">
<head>
<meta charset="utf-8">
<title>Safety Grab Bar Flyer</title>
<link href="https://fonts.googleapis.com/css2?family=Fjalla+One&family=Lilita+One&display=swap" rel="stylesheet">
<style>
  :root {
    --cream: #fdf8d3;
    --red: #ec1f27;
    --deep-red: #c9161d;
    --yellow: #ffe600;
    --black: #111111;
    --white: #ffffff;
  }
  * { margin: 0; padding: 0; box-sizing: border-box; }
  html, body { width: 927px; height: 1200px; overflow: hidden; }
  body { background: var(--cream); }
  .flyer {
    position: relative;
    width: 927px;
    height: 1200px;
    overflow: hidden;
    background: var(--cream);
    font-family: "Fjalla One", "Arial Narrow", sans-serif;
  }
  .abs { position: absolute; }

  .shower-scene {
    left: 44px; top: 224px; width: 440px; height: 640px;
    background: linear-gradient(180deg, #f4f4f2 0%, #e6e6e2 60%, #d9d9d4 100%);
    border-radius: 10px 10px 0 0;
  }

  .headline {
    font-family: "Lilita One", "Arial Black", sans-serif;
    color: var(--black);
    -webkit-text-stroke: 10px var(--white);
    paint-order: stroke fill;
    line-height: 1;
    white-space: nowrap;
    transform-origin: left top;
    transform: scaleX(0.94);
  }
  .headline-1 { left: 76px; top: 70px; font-size: 90px; letter-spacing: -2px; }
  .headline-2 { left: 76px; top: 176px; font-size: 90px; letter-spacing: -2px; }
  .headline-2 .accent { color: var(--red); }

  .bursts { left: 0; top: 0; width: 927px; height: 420px; }

  .burst-text {
    font-family: "Fjalla One", "Arial Narrow", sans-serif;
    text-align: center;
    line-height: 1;
    text-transform: uppercase;
  }
  .burst-hospital { left: 568px; top: 206px; width: 152px; color: var(--red); }
  .burst-hospital .num { font-size: 28px; }
  .burst-hospital .small { font-size: 19px; }
  .burst-hospital .big { font-size: 34px; }
  .burst-hospital .due { font-size: 12px; display: inline-block; line-height: 0.9; vertical-align: 6px; margin-right: 3px; }

  .burst-hip { left: 741px; top: 222px; width: 150px; color: var(--white); }
  .burst-hip .num { font-size: 46px; color: var(--yellow); }
  .burst-hip .small { font-size: 17px; }
  .burst-hip .hl { color: var(--yellow); }
  .burst-hip .big { font-size: 30px; color: var(--yellow); }

  .avoid {
    left: 586px; top: 384px; width: 252px;
    font-family: "Fjalla One", "Arial Narrow", sans-serif;
    font-size: 32px; line-height: 1.05; text-align: center; color: var(--black);
    -webkit-text-stroke: 6px var(--white); paint-order: stroke fill;
    z-index: 3;
  }
  .product-photo {
    left: 604px; top: 414px; width: 216px; height: 216px; border-radius: 50%;
    border: 5px solid var(--yellow);
    background: radial-gradient(circle at 50% 40%, #ffffff 0%, #dfeef8 55%, #b9d6ea 100%);
  }
  .product-label {
    left: 564px; top: 574px; width: 286px; height: 130px;
    background: var(--deep-red); color: var(--white);
    font-family: "Fjalla One", "Arial Narrow", sans-serif;
    font-size: 50px; line-height: 1.02; text-align: center;
    display: flex; align-items: center; justify-content: center;
  }
  .product-note {
    left: 556px; top: 714px; width: 302px;
    font-size: 20px; line-height: 1.2; text-align: center; color: var(--black);
    text-transform: uppercase; white-space: nowrap;
  }

  .price-band { left: 0; top: 780px; width: 927px; height: 420px; }

  .install-copy {
    left: 100px; top: 880px; width: 300px; text-align: right;
    color: var(--white); font-size: 35px; line-height: 1.12; text-transform: uppercase;
  }
  .benefits {
    left: 100px; top: 968px; width: 300px; list-style: none;
    color: var(--white); font-size: 19px; text-transform: uppercase; text-align: right;
  }
  .benefits li { display: inline-block; margin-left: 10px; line-height: 1.7; }
  .benefits .tick { color: var(--yellow); margin-right: 3px; }

  .price {
    left: 424px; top: 800px;
    font-family: "Lilita One", "Arial Black", sans-serif;
    font-size: 262px; line-height: 1; color: var(--white);
    -webkit-text-stroke: 14px var(--black); paint-order: stroke fill;
    letter-spacing: -6px;
  }
  .price sup { font-size: 120px; vertical-align: 110px; margin-left: 4px; }

  .order {
    left: 0; top: 1058px; width: 927px; text-align: center;
    font-family: "Lilita One", "Arial Black", sans-serif;
    color: var(--white); font-size: 46px; line-height: 1;
    display: flex; justify-content: center; align-items: center; gap: 10px;
  }
  .order .phone-icon { width: 42px; height: 42px; }
  .website {
    left: 0; top: 1128px; width: 927px; text-align: center;
    font-family: "Lilita One", "Arial Black", sans-serif;
    color: var(--white); font-size: 30px; line-height: 1;
  }
</style>
</head>
<body>
<main class="flyer">
  <div class="abs shower-scene" role="img" aria-label="Cartoon of a man slipping in the shower, clutching the curtain as he falls backwards"></div>

  <svg class="abs price-band" viewBox="0 0 927 420" aria-hidden="true">
    <path d="M0 110 Q 430 -10 927 40 L927 420 L0 420 Z" fill="var(--red)"/>
  </svg>

  <h1 class="abs headline headline-1">Falls &amp; slip accidents</h1>
  <p class="abs headline headline-2">are <span class="accent">no joke!</span></p>

  <svg class="abs bursts" viewBox="0 0 927 420" aria-hidden="true">
    <g fill="var(--yellow)">
      <rect x="579" y="211" width="130" height="130"/>
      <rect x="579" y="211" width="130" height="130" transform="rotate(15 644 276)"/>
      <rect x="579" y="211" width="130" height="130" transform="rotate(30 644 276)"/>
      <rect x="579" y="211" width="130" height="130" transform="rotate(45 644 276)"/>
      <rect x="579" y="211" width="130" height="130" transform="rotate(60 644 276)"/>
      <rect x="579" y="211" width="130" height="130" transform="rotate(75 644 276)"/>
    </g>
    <g fill="var(--deep-red)">
      <rect x="748" y="224" width="136" height="136"/>
      <rect x="748" y="224" width="136" height="136" transform="rotate(15 816 292)"/>
      <rect x="748" y="224" width="136" height="136" transform="rotate(30 816 292)"/>
      <rect x="748" y="224" width="136" height="136" transform="rotate(45 816 292)"/>
      <rect x="748" y="224" width="136" height="136" transform="rotate(60 816 292)"/>
      <rect x="748" y="224" width="136" height="136" transform="rotate(75 816 292)"/>
    </g>
  </svg>

  <div class="abs burst-text burst-hospital">
    <div class="num">800,000</div>
    <div class="small">Hospitalized</div>
    <div class="big"><span class="due">Due<br>to</span>Fall</div>
    <div class="big">Injury</div>
  </div>

  <div class="abs burst-text burst-hip">
    <div class="num">95%</div>
    <div class="small">Of hip fractures</div>
    <div class="small">Are <span class="hl">caused by</span></div>
    <div class="big">Falling!</div>
  </div>

  <div class="abs product-photo" role="img" aria-label="Photo of a brushed steel safety grab bar"></div>
  <p class="abs avoid">Avoid<br>serious injury<br>with a</p>
  <h2 class="abs product-label">SAFETY<br>GRAB BAR</h2>
  <p class="abs product-note">For your bathroom, by your<br>stairs, or anywhere in your<br>home where slips can happen!</p>

  <p class="abs install-copy">Professionally<br>installed from</p>
  <ul class="abs benefits">
    <li><span class="tick">✔</span>Stability</li>
    <li><span class="tick">✔</span>Extra support</li>
    <li><span class="tick">✔</span>Affordable peace of mind</li>
  </ul>

  <p class="abs price">$99<sup>*</sup></p>

  <p class="abs order">
    <span>Order yours!</span>
    <svg class="phone-icon" viewBox="0 0 24 24" aria-hidden="true">
      <path fill="var(--yellow)" d="M6.6 10.8c1.4 2.8 3.8 5.1 6.6 6.6l2.2-2.2c.3-.3.7-.4 1-.2 1.1.4 2.3.6 3.6.6.6 0 1 .4 1 1V20c0 .6-.4 1-1 1C10.6 21 3 13.4 3 4c0-.6.4-1 1-1h3.5c.6 0 1 .4 1 1 0 1.3.2 2.5.6 3.6.1.3 0 .7-.2 1L6.6 10.8z"/>
    </svg>
    <span>800-555-0147</span>
  </p>
  <p class="abs website">or visit www.safestepathome.com</p>
</main>
</body>
</html>
```